Travel Consultant Business Card

Hello.. New travel consultant looking seeking a business card that incorporates my new logo. I specialize in cruises but also want to imply land vacation. I am very open to any design and font concepts. I'm looking for a very upbeat modern design that reflects cruise and land vacations. Bright vibrant colors

Target Market(s)

Cruise and Land Vacationers

Industry/Entity Type

Travel Agent

Contact Information for Business Card

I am very open to any design and font concepts. I'm looking for a very upbeat modern design that reflects cruise and land vacations. Bright vibrant colors

Colors

Designer to choose colors to be used in the design.

Requirements
Must have
• Company Name: MapleRidge Journeys---New logo uploaded to be included in design
• My Name: Dolores Kwiatek-Travel Consultant
• Phone Number: (555) 418-7093
• E-Mail Address: mapleridgejourneys@examplemail.net
• Website: www.mapleridgejourneys.example
Nice to have
• My tag line is …..Here to Get You There

```html
<!DOCTYPE html>
<html lang="en">
<head>
<meta charset="utf-8">
<title>MapleRidge Journeys – Business Card</title>
<link rel="stylesheet" href="https://fonts.googleapis.com/css2?family=Raleway:wght@700;800&family=Open+Sans:wght@400;600&display=swap">
<style>
  :root {
    --backdrop: #b7b2b3;
    --paper: #ffffff;
    --blue-deep: #1463b5;
    --blue: #1a72c2;
    --sky: #29a6e0;
    --sky-light: #3cb6ea;
    --brand: #1f6fc2;
    --white: #ffffff;
  }
  * { box-sizing: border-box; margin: 0; padding: 0; }
  html, body {
    width: 1061px; height: 1200px; overflow: hidden;
    background: var(--backdrop);
  }
  .sheet {
    width: 1061px; height: 1200px;
    display: flex; flex-direction: column; align-items: center; justify-content: center;
    gap: 60px;
  }
  .card {
    position: relative;
    width: 900px; height: 514px;
    background: var(--paper);
    overflow: hidden;
  }
  .brand-name {
    font-family: "Raleway", sans-serif;
    font-weight: 800;
    color: var(--brand);
    white-space: nowrap;
    letter-spacing: -0.5px;
    position: absolute; left: 0; right: 0; text-align: center;
  }
  /* Front */
  .card--front .brand-name { top: 200px; font-size: 58px; }
  .front-band { position: absolute; left: 0; bottom: 0; width: 900px; height: 44px; }

  /* Back */
  .card--back .brand-name { top: 80px; font-size: 46px; }
  .back-field {
    position: absolute; left: 0; top: 236px; width: 900px; height: 278px;
    background: var(--blue);
    border-top: 22px solid var(--blue-deep);
  }
  .name-panel {
    position: absolute; left: -6px; top: 260px; width: 410px; height: 270px;
    background: var(--sky);
    border-top: 5px solid var(--white);
    border-right: 5px solid var(--white);
    border-top-right-radius: 110px;
    display: flex; flex-direction: column; align-items: center; justify-content: center;
    padding-bottom: 14px;
    color: var(--white);
    font-family: "Raleway", sans-serif;
    font-weight: 700;
  }
  .consultant-name { font-size: 31px; line-height: 1.15; }
  .consultant-title { font-size: 22px; }
  .contact-list {
    position: absolute; left: 430px; top: 278px; width: 450px;
    list-style: none;
  }
  .contact-list::before {
    content: ""; position: absolute; left: 17px; top: 24px; bottom: 24px;
    width: 2px; background: var(--sky-light);
  }
  .contact-item {
    position: relative;
    display: flex; align-items: center; gap: 14px;
    height: 66px;
    font-family: "Open Sans", sans-serif;
    font-size: 21px;
    color: var(--white);
    white-space: nowrap;
  }
  .contact-icon {
    flex: none; width: 36px; height: 36px; border-radius: 50%;
    background: var(--sky-light);
    display: flex; align-items: center; justify-content: center;
  }
  .contact-icon svg { width: 20px; height: 20px; }
</style>
</head>
<body>
<main class="sheet">

  <section class="card card--front" aria-label="Card front">
    <p class="brand-name">MapleRidge Journeys</p>
    <svg class="front-band" viewBox="0 0 900 44" preserveAspectRatio="none" aria-hidden="true">
      <rect width="900" height="44" fill="var(--sky)"/>
      <path d="M0 0 H300 C340 0 380 20 420 44 H0 Z" fill="var(--blue-deep)"/>
      <path d="M300 0 C350 0 395 18 440 44" stroke="var(--white)" stroke-width="5" fill="none"/>
    </svg>
  </section>

  <section class="card card--back" aria-label="Card back">
    <p class="brand-name">MapleRidge Journeys</p>
    <div class="back-field"></div>
    <div class="name-panel">
      <p class="consultant-name">Dolores Kwiatek</p>
      <p class="consultant-title">Travel Consultant</p>
    </div>
    <ul class="contact-list">
      <li class="contact-item">
        <span class="contact-icon">
          <svg viewBox="0 0 24 24" aria-hidden="true"><path fill="#fff" d="M6.6 10.8a15.1 15.1 0 0 0 6.6 6.6l2.2-2.2a1 1 0 0 1 1-.25 11.4 11.4 0 0 0 3.6.57 1 1 0 0 1 1 1V20a1 1 0 0 1-1 1A17 17 0 0 1 3 4a1 1 0 0 1 1-1h3.5a1 1 0 0 1 1 1c0 1.25.2 2.45.57 3.57a1 1 0 0 1-.25 1z"/></svg>
        </span>
        (555) 418-7093
      </li>
      <li class="contact-item">
        <span class="contact-icon">
          <svg viewBox="0 0 24 24" aria-hidden="true"><rect x="3" y="6" width="18" height="12" rx="1" fill="none" stroke="#fff" stroke-width="1.8"/><path d="M3 6l9 7 9-7M3 18l7-6M21 18l-7-6" fill="none" stroke="#fff" stroke-width="1.6"/></svg>
        </span>
        mapleridgejourneys@examplemail.net
      </li>
      <li class="contact-item">
        <span class="contact-icon">
          <svg viewBox="0 0 24 24" aria-hidden="true"><g fill="none" stroke="#fff" stroke-width="1.6"><circle cx="12" cy="12" r="9"/><ellipse cx="12" cy="12" rx="4" ry="9"/><path d="M3 12h18M5 7h14M5 17h14"/></g></svg>
        </span>
        www.mapleridgejourneys.example
      </li>
    </ul>
  </section>

</main>
</body>
</html>
```